Banner for promote service of debit card

We are PagaVelo and we need the banners to be posted on the facebook and instagram pages.
We want something to communicate that it is an exclusive debit card full of services.
Low commissions.
Our competitors:
https://www.nortapay-pagos.it/it/home.html
https://www.zelkor-conti.it/it/
https://www.fotoreelz.it/serravanbank/
sendquillo
maybe some banner that makes the idea of a convenient debit card that everyone can use.
Girls enjoying card shopping.
Please check also website for slogans and phrases to use
https://www.pagavelo-carta.it/
Should show the services.
We must convey that it is a fast, simple card that guarantees privacy.
We need strong banners that attract people as these ban will be sponsored on instagram and facebook
Target Market(s)
People 18-35 y
Open Bank account. low commissions. Easy to use. No limits. 100% Privacy.
Requirements
Must have
- Written in Italian.

```html
<!DOCTYPE html>
<html lang="it">
<head>
<meta charset="UTF-8">
<title>PagaVelo – Una carta per tutti</title>
<link href="https://fonts.googleapis.com/css2?family=Montserrat:ital,wght@0,300;0,700;0,800;1,800&display=swap" rel="stylesheet">
<style>
  :root {
    --bg-deep: #1c0b4f;
    --bg-mid: #2e1266;
    --bg-glow: #d8183c;
    --white: #ffffff;
    --yellow: #fde58a;
    --blue: #3aa7cf;
    --cyan: #45c0d8;
    --orange: #ee6a3c;
    --ink: #1a1030;
  }
  * { margin: 0; padding: 0; box-sizing: border-box; }
  html, body { width: 1200px; height: 558px; overflow: hidden; }
  body { font-family: 'Montserrat', sans-serif; }

  .banner {
    position: relative;
    width: 1200px;
    height: 558px;
    overflow: hidden;
    background:
      radial-gradient(ellipse 360px 260px at 1200px 540px, var(--bg-glow) 0%, rgba(216,24,60,0) 70%),
      radial-gradient(ellipse 500px 400px at 620px 300px, var(--bg-mid) 0%, rgba(46,18,102,0) 80%),
      linear-gradient(120deg, var(--bg-deep) 0%, #26105c 55%, #3a1670 100%);
  }

  .triangle-field {
    position: absolute;
    left: 0; top: 0;
    width: 430px; height: 558px;
  }

  .headline {
    position: absolute;
    right: 528px;
    top: 66px;
    text-align: right;
    line-height: 1;
  }
  .headline-main {
    display: block;
    font-weight: 800;
    font-size: 78px;
    color: var(--white);
    letter-spacing: -1px;
  }
  .headline-card {
    display: block;
    margin-top: 20px;
    font-weight: 800;
    font-size: 68px;
    color: var(--yellow);
  }
  .headline-all {
    display: block;
    margin-top: 22px;
    font-weight: 300;
    font-size: 56px;
    color: var(--white);
  }

  .claims {
    position: absolute;
    right: 528px;
    top: 332px;
    display: flex;
    flex-direction: column;
    align-items: flex-end;
    gap: 9px;
    list-style: none;
  }
  .claim {
    height: 32px;
    padding: 0 8px 0 9px;
    border-radius: 9px;
    font-weight: 800;
    font-style: italic;
    font-size: 20px;
    line-height: 32px;
    color: var(--ink);
    white-space: nowrap;
  }
  .claim--blue { background: var(--blue); }
  .claim--yellow { background: var(--yellow); }
  .claim--cyan { background: var(--cyan); }
  .claim--orange { background: var(--orange); }

  .shopper-photo {
    position: absolute;
    left: 694px; top: 0;
    width: 506px; height: 558px;
  }

  .brand-name {
    position: absolute;
    right: 42px;
    top: 90px;
    font-weight: 700;
    font-size: 34px;
    line-height: 1;
    color: var(--white);
  }
</style>
</head>
<body>
  <main class="banner">
    <svg class="triangle-field" viewBox="0 0 430 558" role="img" aria-label="Motivo decorativo di triangoli colorati viola, turchesi, rosa e gialli">
      <defs>
        <linearGradient id="triangleTones" x1="0" y1="0" x2="0.6" y2="1">
          <stop offset="0" stop-color="#7a3fc4"/>
          <stop offset="0.35" stop-color="#5a7fd6"/>
          <stop offset="0.55" stop-color="#2fc2b0"/>
          <stop offset="0.75" stop-color="#9a5fd0"/>
          <stop offset="1" stop-color="#f2cf2a"/>
        </linearGradient>
      </defs>
      <polygon points="0,0 150,0 110,120 210,270 170,320 330,300 420,410 340,558 0,558" fill="url(#triangleTones)"/>
    </svg>

    <h1 class="headline">
      <span class="headline-main">ALL IN ONE !</span>
      <span class="headline-card">UNA CARTA</span>
      <span class="headline-all">PER TUTTI</span>
    </h1>

    <ul class="claims">
      <li class="claim claim--blue">ENJOY YOUR CART!</li>
      <li class="claim claim--yellow">FAI QUELLO CHE VUOI.</li>
      <li class="claim claim--cyan">NESSUN LIMITE</li>
      <li class="claim claim--orange">NESSUN CONTROLLO.</li>
    </ul>

    <svg class="shopper-photo" viewBox="0 0 506 558" role="img" aria-label="Foto di una ragazza sorridente con maglia a righe che mostra una carta di debito e porta buste della spesa colorate">
      <defs>
        <linearGradient id="shopperTones" x1="0" y1="0" x2="1" y2="1">
          <stop offset="0" stop-color="#3a1a55"/>
          <stop offset="0.45" stop-color="#8a8fa0"/>
          <stop offset="0.75" stop-color="#9fd8c8"/>
          <stop offset="1" stop-color="#f3e7c0"/>
        </linearGradient>
      </defs>
      <path d="M110,558 L100,300 L130,120 L200,20 L300,20 L380,150 L506,230 L506,558 Z" fill="url(#shopperTones)" opacity="0.85"/>
    </svg>

    <span class="brand-name">PagaVelo</span>
  </main>
</body>
</html>
```